Legal Agribusiness Capability Brochure Design

Design A4 sized 6 page Legal Agribusiness Capability Brochure. Design is to be consistent with current marketing materials - logo, letterhead, website and business card to be provided.
Cover page - Firm name and logo, Agribusiness Capability Statement heading with image 1 below
Inside cover page - About Us section with image 2 below then Awards section below image
Inside middle page - Our Expertise with image 3 below
Inside back page - Our Experience with image 4 below
Back page - Senior Lawyers with image 5 below
Outside Middle Back Page - Contact Us with image 6
Updates

To provide more details to designers for brochure

Target Market(s)

Agribusiness - Australia

Industry/Entity Type

Legal

Colors

Designer to choose colors to be used in the design.

Requirements
Must have
• Use content from uloaded file - Agribusiness Brochure Content
• Use images uploaded
• Professional appearance
• Consistent with current marketing and website https://ferngatelegal.com.au/

```html
<!DOCTYPE html>
<html lang="en">
<head>
<meta charset="utf-8">
<title>Ferngate Legal – Agribusiness Capability Brochure Spread</title>
<link href="https://fonts.googleapis.com/css2?family=Roboto+Condensed:wght@700&family=Nunito+Sans:wght@400;500&display=swap" rel="stylesheet">
<style>
  :root{
    --brand-blue:#1aa6dc;
    --ink:#222222;
    --muted-grey:#8a8a8a;
    --paper:#f4f4f4;
    --footer-dark:#363636;
    --backdrop:#e4e4e4;
    --badge-gold:#e7dcae;
  }
  *{margin:0;padding:0;box-sizing:border-box}
  html,body{width:1200px;height:919px;overflow:hidden;background:var(--backdrop)}
  body{font-family:"Nunito Sans",Arial,sans-serif;color:var(--ink)}
  .spread{position:absolute;left:40px;top:49px;width:1120px;height:820px;display:flex}
  .page{position:relative;width:560px;height:820px;background:var(--paper);overflow:hidden}
  .page--left{border-right:1px solid #d6d6d6}

  .photo{position:absolute;left:0;top:560px;width:560px;height:243px}
  .photo--canola{background:linear-gradient(180deg,#a9bcc8 0%,#c5cfc4 22%,#d9e13a 36%,#9fbf4a 55%,#5e8a3a 75%,#3d6a2c 100%)}
  .photo--cattle{background:radial-gradient(ellipse at 55% 40%,#b48a55 0%,#6e4d2c 45%,#2a1d12 100%)}
  .page-shape{position:absolute;left:0;top:0}
  .footer-strip{position:absolute;left:0;bottom:0;width:560px;height:20px;background:var(--footer-dark)}

  .header .seal{position:absolute;left:28px;top:20px;width:86px;height:86px;border-radius:50%;border:3px solid #333}
  .header .listing-badge{position:absolute;left:450px;top:28px;width:78px;height:78px;border-radius:50%;background:var(--badge-gold);opacity:.7}
  .brand{position:absolute;left:154px;top:34px;display:flex;align-items:center;gap:12px}
  .brand__mark{width:98px;height:62px;background:var(--brand-blue);border-radius:10px}
  .brand__name{font-family:"Nunito Sans",Arial,sans-serif;font-weight:500;color:var(--brand-blue);font-size:25px;line-height:25px;letter-spacing:.5px}
  .brand__tagline{position:absolute;left:264px;top:92px;font-size:12px;color:var(--muted-grey)}

  .section-title{position:absolute;font-family:"Roboto Condensed",Arial,sans-serif;font-weight:700;font-size:21px;color:var(--brand-blue);letter-spacing:.3px}
  .bullets{position:absolute;list-style:none;font-size:10.5px;line-height:13.7px}
  .bullets li{position:relative;padding-left:12px}
  .bullets li::before{content:"";position:absolute;left:0;top:3px;border-left:7px solid var(--brand-blue);border-top:4px solid transparent;border-bottom:4px solid transparent}
  .prose{position:absolute;font-size:10.5px;line-height:11.5px;text-align:justify;text-indent:16px}
</style>
</head>
<body>
<main class="spread">

  <section class="page page--left">
    <div class="photo photo--canola" role="img" aria-label="Photograph of flowering yellow canola fields and green farmland under a pale sky"></div>
    <svg class="page-shape" width="560" height="600" viewBox="0 0 560 600" aria-hidden="true">
      <path d="M0 0 H560 V470 Q560 598 470 600 H0 Z" fill="var(--brand-blue)"/>
      <path d="M0 0 H560 V462 Q560 590 470 592 H0 Z" fill="var(--paper)"/>
    </svg>
    <div class="footer-strip"></div>

    <header class="header">
      <div class="seal"></div>
      <div class="brand"><div class="brand__mark"></div><div class="brand__name">FERNGATE<br>LEGAL</div></div>
      <div class="brand__tagline">Commercial + Litigation</div>
      <div class="listing-badge"></div>
    </header>

    <h2 class="section-title" style="left:75px;top:152px">ABOUT US</h2>
    <ul class="bullets" style="left:43px;top:194px;width:440px">
      <li>Independent commercial law firm with offices in Kallara and Brookmere</li>
      <li>Senior lawyers offering a combined 65 years of legal experience</li>
      <li>Practical advice in a professional and timely manner</li>
      <li>Client relationships built on trust</li>
      <li>Unfettered access to senior lawyers</li>
      <li>Direct and ongoing partner level involvement for each client</li>
      <li>Utilise the best information technology available to maintain high levels of efficiency and confidentiality</li>
    </ul>

    <h2 class="section-title" style="left:77px;top:318px">AGRIBUSINESS LEGAL AWARDS</h2>
    <ul class="bullets" style="left:43px;top:364px;width:470px">
      <li>Ranked as a “Leading Agribusiness Law Firm - Westland, 2019” (Top 4)</li>
      <li>Ranked as a “Leading Agribusiness Law Firm - Westland, 2018” (Top 4)</li>
      <li>Ranked as a “Leading Agribusiness Law Firm - Westland, 2017” (Top 5)</li>
    </ul>

    <h2 class="section-title" style="left:77px;top:430px">QUALITY PRACTICE STANDARD</h2>
    <p class="prose" style="left:39px;top:472px;width:474px">We are part of a select group of law firms which has been awarded the Quality Practice Standard by the Westland Law Society. As a result, we are able to better serve our clients by:</p>
    <ul class="bullets" style="left:43px;top:506px;width:470px">
      <li>Adopting modern quality management principles;</li>
      <li>Focusing on clients’ requirements and client care; and</li>
      <li>Striving for consistency of service for all clients by all at the firm.</li>
    </ul>
  </section>

  <section class="page page--right">
    <div class="photo photo--cattle" role="img" aria-label="Photograph of a stockman on horseback silhouetted against dust with cattle in a yard at dusk"></div>
    <svg class="page-shape" width="560" height="600" viewBox="0 0 560 600" aria-hidden="true">
      <path d="M0 470 Q0 598 90 600 H560 V0 H0 Z" fill="var(--brand-blue)"/>
      <path d="M0 462 Q0 590 90 592 H560 V0 H0 Z" fill="var(--paper)"/>
    </svg>
    <div class="footer-strip"></div>

    <header class="header">
      <div class="seal"></div>
      <div class="brand"><div class="brand__mark"></div><div class="brand__name">FERNGATE<br>LEGAL</div></div>
      <div class="brand__tagline">Commercial + Litigation</div>
      <div class="listing-badge"></div>
    </header>

    <h2 class="section-title" style="left:86px;top:152px">EXPERTISE</h2>
    <p class="prose" style="left:52px;top:198px;width:462px">Over several decades our senior lawyers have advised clients involved in wheat, canola, lupin, wool, beef, dairy, wool, lamb, poultry, piggery, viticulture, forestry and plantation businesses.</p>
    <p class="prose" style="left:52px;top:231px;width:462px">Our senior lawyers have strong family connections with pastoralists which allows them to better appreciate the challenges faced in agribusiness.</p>
    <p class="prose" style="left:52px;top:264px;width:462px">Our family connection with pastoralists and our strong technical expertise in agribusiness law places Ferngate Legal in a unique position to advise clients in the agribusiness industry.</p>
    <p class="prose" style="left:52px;top:304px;width:462px">We can assist with the following agribusiness matters:</p>
    <ul class="bullets" style="left:52px;top:341px;width:480px">
      <li>Agribusiness property contracts, agreements and deeds;</li>
      <li>Sale and purchase of agribusiness and farm assets;</li>
      <li>Pastoral lease advice;</li>
      <li>Native Title advice concerning access and compensation agreements;</li>
      <li>Land access agreements with mining, energy and telecommunications companies;</li>
      <li>Partnership, trust, corporation and joint venture advice;</li>
      <li>Farm Leases, Share Farming Agreements and Livestock Management Agreements;</li>
      <li>Carbon trading advice;</li>
      <li>Mortgages and securities;</li>
      <li>Farm succession planning, including Wills, Enduring Powers of Attorney and Guardianship;</li>
      <li>Employment advice;</li>
      <li>Deceased estates and probate, including advice concerning family provision claims; and</li>
      <li>Disputes.</li>
    </ul>
  </section>

</main>
</body>
</html>
```